Need a redesign for our Wordpress Credit report website

Hi, We need someone to redesign our Wordpress credit report website, brightledgerview.co.za. The designer will be responsible for the following pages:
- home page
- blog page
- single post
- dashboard
- credit report page

About BrightLedgerView.co.za
Bright Ledger View is a consumer focussed credit report platform where South African citizens can get an easy to understand credit report that shows them where to improve their credit scores.

```html
<!DOCTYPE html>
<html lang="en">
<head>
<meta charset="utf-8">
<title>Bright Ledger View – Check Your Credit Score</title>
<link href="https://fonts.googleapis.com/css2?family=Montserrat:wght@400;500;600;700&display=swap" rel="stylesheet">
<style>
:root{
  --blue:#2c6fd1;
  --blue-deep:#1f5fbf;
  --green:#8cc63f;
  --green-soft:#d9ecc0;
  --ink:#1b1b1b;
  --muted:#6b6b6b;
  --line:#d6d6d6;
  --hero-bg:#eef2f7;
  --section-bg:#f0f5fb;
  --card-border:#e6e9ee;
  --white:#ffffff;
  --star:#f5b800;
}
*{box-sizing:border-box;margin:0;padding:0}
html,body{width:1200px;height:4172px;overflow:hidden}
body{position:relative;font-family:'Montserrat',sans-serif;color:var(--ink);background:var(--white)}
.abs{position:absolute}
.hero{left:0;top:0;width:1200px;height:729px;background:linear-gradient(180deg,#f4f7fb 0%,var(--hero-bg) 100%);overflow:hidden}
.slash{position:absolute}
.brand{left:100px;top:28px;display:flex;align-items:center;gap:10px}
.brand-dot{width:46px;height:46px;border-radius:50%;background:var(--green)}
.brand-name{font-size:24px;font-weight:600;color:var(--blue)}
.nav{top:24px;left:562px;display:flex;gap:0}
.nav a{position:absolute;top:0;font-size:15px;color:var(--ink);text-decoration:none;white-space:nowrap}
.nav a.active{color:var(--green);border-bottom:2px solid var(--green);padding-bottom:3px}
.login{left:962px;top:13px;width:138px;height:42px;border:2px solid var(--blue);border-radius:21px;color:var(--blue);font-weight:600;font-size:15px;display:flex;align-items:center;justify-content:center;gap:6px}
.hero-art{left:0;top:243px;width:413px;height:340px;background:linear-gradient(160deg,#ffffff 0%,#dfe6f0 100%);border-radius:0 10px 10px 0}
.hero-title{left:300px;top:190px;width:460px;text-align:center;font-size:39px;font-weight:700;line-height:40px}
.hero-title span{display:block;color:var(--blue)}
.checks{left:405px;top:312px;list-style:none}
.checks li{font-size:14px;height:31.5px;display:flex;align-items:center;gap:8px}
.tick{width:16px;height:16px;border-radius:50%;background:var(--green);display:inline-flex;align-items:center;justify-content:center}
.form{left:764px;top:92px;width:336px;height:512px;background:var(--white);border:1px solid #e2e6ec;border-radius:8px;box-shadow:0 4px 14px rgba(0,0,0,.06);overflow:hidden}
.form-head{height:49px;background:var(--green);color:#fff;font-size:24px;font-weight:600;display:flex;align-items:center;justify-content:center}
.field{position:absolute;left:20px;width:296px;font-size:13px;color:#555;border-bottom:1px solid var(--line);height:30px}
.agree{position:absolute;left:20px;top:350px;font-size:10.5px;color:#555;display:flex;align-items:center;gap:5px}
.agree i{width:11px;height:11px;border:1px solid #999;display:inline-block}
.show-btn{position:absolute;left:20px;top:379px;width:293px;height:42px;border-radius:21px;background:var(--blue);color:#fff;font-weight:700;font-size:15px;display:flex;align-items:center;justify-content:center}
.fine{position:absolute;left:20px;top:440px;width:296px;font-size:10.5px;line-height:18px;color:#777}
.sec-title{left:0;width:1200px;text-align:center;font-size:40px;font-weight:700}
.sec-title span{color:var(--blue)}
.feature{width:238px;height:169px;background:#fff;border:1px solid var(--card-border);box-shadow:0 2px 8px rgba(0,0,0,.04);text-align:center;font-size:13.5px;line-height:21px;color:#555}
.feature svg{display:block;margin:28px auto 12px}
.why{left:0;top:1280px;width:1200px;height:1530px;background:var(--section-bg);overflow:hidden}
.illus{border-radius:12px}
.why-icon{width:78px;height:78px;border-radius:50%;background:#dde9f7;display:flex;align-items:center;justify-content:center}
.why-h{font-size:25px;font-weight:600;line-height:29px}
.why-p{font-size:13px;line-height:25px;color:#666;text-align:justify}
.reviews-title{left:99px;top:2898px;font-size:40px;font-weight:700}
.reviews-title span{color:var(--blue)}
.review{width:313px;height:220px;background:#fff;box-shadow:0 3px 12px rgba(0,0,0,.1);padding:58px 20px 0 20px}
.avatar{width:68px;height:68px;border-radius:50%;background:linear-gradient(135deg,#c9a98e,#7a5a45);border:3px solid #fff;box-shadow:0 1px 4px rgba(0,0,0,.15)}
.review h4{font-size:16px;font-weight:700}
.review small{display:block;font-size:10.5px;color:#555;margin-top:2px}
.review p{font-size:12.5px;line-height:24px;color:#777;margin-top:10px;text-align:justify}
.stars{color:var(--star);font-size:16px;letter-spacing:1px;margin-top:8px}
.testi{left:0;top:3303px;width:1200px;height:521px;background:var(--section-bg);overflow:hidden}
.t-avatar{width:88px;height:88px;border-radius:50%;background:linear-gradient(135deg,#dcdcdc,#8a8a8a);border:3px solid var(--blue)}
.t-text{width:434px;text-align:center;font-size:12.5px;line-height:24px;color:#777}
.footer{left:0;top:3824px;width:1200px;height:348px;background:var(--blue-deep);color:#fff}
.footer h5{position:absolute;top:82px;font-size:15px;font-weight:600}
.footer a{position:absolute;font-size:13px;color:#e6eefb;text-decoration:none}
.news{position:absolute;left:836px;top:108px;width:264px;height:30px;border-bottom:1px solid #9db9e6;font-size:13px}
.social{position:absolute;width:37px;height:37px;border:1.5px solid #fff;border-radius:50%}
.divider{position:absolute;left:99px;top:235px;width:1001px;height:1px;background:#4f81cf}
.copy{position:absolute;left:99px;top:295px;font-size:12.5px}
.pay{position:absolute;top:287px;width:52px;height:34px;background:#fff;border-radius:4px}
</style>
</head>
<body>

<section class="abs hero">
  <svg class="slash" style="left:0;top:0" width="1200" height="729" aria-hidden="true">
    <polygon points="0,150 80,130 55,175 0,185" fill="var(--green-soft)"/>
    <polygon points="0,690 110,660 95,700 0,729" fill="var(--green)"/>
    <polygon points="1090,520 1200,495 1200,560 1075,575" fill="var(--green-soft)"/>
  </svg>
  <div class="abs hero-art" role="img" aria-label="Laptop displaying an example credit report with a score gauge"></div>
</section>

<header>
  <div class="abs brand"><span class="brand-dot"></span><span class="brand-name">Bright Ledger View</span></div>
  <nav class="abs nav">
    <a class="active" style="left:0">Home</a>
    <a style="left:98px">Articles</a>
    <a style="left:209px">About</a>
    <a style="left:308px">Contact</a>
  </nav>
  <div class="abs login">
    <svg width="12" height="13" viewBox="0 0 12 13"><circle cx="6" cy="3.5" r="3" fill="var(--blue)"/><path d="M0 13c0-4 2.5-6 6-6s6 2 6 6z" fill="var(--blue)"/></svg>LOGIN
  </div>
</header>

<h1 class="abs hero-title">Check Your Credit<span>Score Within Seconds</span></h1>
<ul class="abs checks">
  <li><span class="tick"><svg width="9" height="7"><path d="M1 3.5l2.5 2.5L8 1" stroke="#fff" stroke-width="1.6" fill="none"/></svg></span>See your most recent credit score</li>
  <li><span class="tick"><svg width="9" height="7"><path d="M1 3.5l2.5 2.5L8 1" stroke="#fff" stroke-width="1.6" fill="none"/></svg></span>Get access to your full credit profile</li>
  <li><span class="tick"><svg width="9" height="7"><path d="M1 3.5l2.5 2.5L8 1" stroke="#fff" stroke-width="1.6" fill="none"/></svg></span>See who has been looking at your profile</li>
  <li><span class="tick"><svg width="9" height="7"><path d="M1 3.5l2.5 2.5L8 1" stroke="#fff" stroke-width="1.6" fill="none"/></svg></span>See if you have any adverse or Blacklistings</li>
</ul>

<form class="abs form">
  <div class="form-head">Get Started Now</div>
  <div class="field" style="top:72px">ID Number</div>
  <div class="field" style="top:130px">First Name</div>
  <div class="field" style="top:186px">Last Name</div>
  <div class="field" style="top:244px">Primary Email</div>
  <div class="field" style="top:301px">Mobile Number</div>
  <div class="agree"><i></i>I agree with the terms and conditions</div>
  <div class="show-btn">SHOW MY SCORE</div>
  <p class="fine">By signing up &amp; agreeing with the terms you authorise BrightLedgerView.co.za to request your credit report from the bureaus and display it within the site.</p>
</form>

<h2 class="abs sec-title" style="top:730px">System <span>Features</span></h2>
<div class="abs feature" style="left:99px;top:811px"><svg width="56" height="50" fill="none" stroke="var(--blue)" stroke-width="2"><circle cx="14" cy="16" r="7"/><circle cx="42" cy="16" r="7"/><path d="M4 46v-12h20v12M32 46v-12h20v12M20 6l16 16M36 6L20 22" stroke="var(--green)"/></svg>Dispute generator - easily<br>manage disputes</div>
<div class="abs feature" style="left:353px;top:811px"><svg width="56" height="56" fill="none" stroke="var(--blue)" stroke-width="2"><circle cx="26" cy="26" r="22"/><path d="M26 4v22h22"/><rect x="32" y="34" width="20" height="16" stroke="var(--green)"/></svg>Budget tool - easily create<br>a budget</div>
<div class="abs feature" style="left:606px;top:811px"><svg width="44" height="56" fill="none" stroke="var(--blue)" stroke-width="2"><rect x="4" y="2" width="36" height="50" rx="3"/><path d="M12 12h20M12 20h20M12 28h20" stroke="var(--green)"/><path d="M12 38h20M12 44h12"/></svg>Improve your credit score<br>eBook</div>
<div class="abs feature" style="left:860px;top:811px"><svg width="56" height="56" fill="none" stroke="var(--blue)" stroke-width="2"><path d="M10 14l6-10h14l6 10z"/><circle cx="23" cy="34" r="16"/><path d="M23 24v20M28 28h-8v6h6v6h-8" stroke="var(--green)"/><rect x="40" y="26" width="14" height="22"/></svg>Personal Budgeting<br>Spreadsheet</div>
<div class="abs feature" style="left:227px;top:996px"><svg width="64" height="52" fill="none" stroke="var(--blue)" stroke-width="2"><rect x="14" y="2" width="48" height="36"/><rect x="8" y="8" width="48" height="36" fill="#fff"/><rect x="2" y="14" width="48" height="36" fill="#fff"/><path d="M20 26v12l10-6z" fill="var(--green)" stroke="var(--green)"/></svg>Perfect score video<br>course</div>
<div class="abs feature" style="left:481px;top:996px"><svg width="64" height="52" fill="none" stroke="var(--blue)" stroke-width="2"><rect x="6" y="4" width="52" height="36"/><path d="M2 46h60"/><circle cx="24" cy="20" r="6" stroke="var(--green)"/><path d="M14 36c0-6 5-9 10-9s10 3 10 9M40 14h12M40 22h12" /></svg>Personal Finance Video<br>Tutorials</div>
<div class="abs feature" style="left:734px;top:996px"><svg width="60" height="54" fill="none" stroke="var(--blue)" stroke-width="2"><circle cx="22" cy="28" r="12"/><path d="M6 28a16 16 0 0 1 32 0M6 28v8M38 28v8"/><rect x="36" y="2" width="22" height="16" rx="3" stroke="var(--green)"/><path d="M10 52c2-6 6-8 12-8s10 2 12 8"/></svg>Dedicated<br>24/7 Support</div>

<section class="abs why">
  <svg style="position:absolute;left:0;top:0" width="1200" height="1530" aria-hidden="true">
    <polygon points="1040,0 1200,-40 1200,40 1030,30" fill="var(--green)"/>
    <polygon points="30,60 200,35 185,90 10,120" fill="var(--green-soft)"/>
    <polygon points="1075,35 1200,10 1200,60 1060,65" fill="var(--green-soft)"/>
  </svg>
</section>
<h2 class="abs sec-title" style="top:1412px">Why Get Your <span>Score From Us?</span></h2>

<div class="abs illus" style="left:146px;top:1530px;width:380px;height:373px;background:linear-gradient(160deg,#e3ebf6,#c9d9ef)" role="img" aria-label="Illustration of a woman signing up on a large phone beside a padlock"></div>
<div class="abs why-icon" style="left:622px;top:1568px"><svg width="40" height="30" fill="none" stroke="var(--blue)" stroke-width="2"><path d="M4 26a16 16 0 0 1 32 0"/><path d="M20 26l8-10" stroke="var(--green)"/><circle cx="20" cy="26" r="2"/></svg></div>
<h3 class="abs why-h" style="left:622px;top:1653px;width:430px">We don't abuse your personal information:</h3>
<p class="abs why-p" style="left:622px;top:1717px;width:428px">Companies that give out free credit scores use your personal information to sell you financial products. That's how they can afford to give it to you for free. We believe that your personal information should be protected and not abused. That's why we ask a small fee. It enables us to protect your information and not abuse it.</p>

<div class="abs why-icon" style="left:173px;top:2022px"><svg width="38" height="36" fill="none" stroke="var(--blue)" stroke-width="2"><rect x="8" y="6" width="26" height="28"/><path d="M12 26l6-6 4 4 8-8" stroke="var(--green)"/><circle cx="8" cy="8" r="6"/></svg></div>
<h3 class="abs why-h" style="left:173px;top:2106px;width:430px">Our report is super easy to understand:</h3>
<p class="abs why-p" style="left:173px;top:2170px;width:428px">Our credit report is one of the easiest reports to understand. The report is clearly laid out and you will see immediately if you can apply for finance, if you are blacklisted, and where you can improve.</p>
<div class="abs illus" style="left:688px;top:1959px;width:340px;height:364px;background:linear-gradient(160deg,#e3ebf6,#c9d9ef)" role="img" aria-label="Illustration of a woman holding a bank card beside a phone checkout screen"></div>

<div class="abs illus" style="left:170px;top:2388px;width:356px;height:324px;background:linear-gradient(160deg,#e3ebf6,#c9d9ef)" role="img" aria-label="Illustration of a person on a sofa with a report, score gauge and coins"></div>
<div class="abs why-icon" style="left:630px;top:2434px"><svg width="40" height="30" fill="none" stroke="var(--blue)" stroke-width="2"><path d="M2 12l8-6 10 6 10-6 8 6-18 14z"/><path d="M14 16l6 5 6-5" stroke="var(--green)"/></svg></div>
<h3 class="abs why-h" style="left:630px;top:2517px;width:430px">300,000 + South Africans have trusted us:</h3>
<p class="abs why-p" style="left:630px;top:2580px;width:428px">Since 2008 we have helped over 300,000 South Africans make sense of their credit reports, so you can rest assured knowing that we have a proven track record and that you are in safe hands with us.</p>

<h2 class="abs reviews-title">Verified <span>Reviews</span></h2>
<svg class="abs" style="left:1028px;top:2918px" width="72" height="16" aria-hidden="true"><path d="M2 8h28M2 8l6-5M2 8l6 5M42 8h28M70 8l-6-5M70 8l-6 5" stroke="#333" stroke-width="1.5" fill="none"/></svg>

<div class="abs review" style="left:113px;top:3020px"><h4>Lindiwe Mokoena</h4><small>28 reviews</small><p>Their customer support team has been very impressive. The tools and knowledge they shared were of great practical use.</p><div class="stars">★★★★★</div></div>
<div class="abs avatar" style="left:100px;top:2989px" role="img" aria-label="Reviewer portrait"></div>
<div class="abs review" style="left:510px;top:3020px"><h4>Ridgeway Fitness ZA</h4><small>28 reviews</small><p>Excellent credit report service. They respond to queries promptly, and have a very detailed credit report</p><div class="stars">★★★★★</div></div>
<div class="abs avatar" style="left:497px;top:2989px" role="img" aria-label="Reviewer portrait"></div>
<div class="abs review" style="left:907px;top:3020px;width:320px"><h4>Lindiwe Mokoena</h4><small>28 reviews</small><p>Their customer support team has been very impressive. The tools and knowledge they shared were of great practical use.</p><div class="stars">★★★★★</div></div>
<div class="abs avatar" style="left:894px;top:2989px" role="img" aria-label="Reviewer portrait"></div>
<svg class="abs" style="left:1100px;top:3230px" width="100" height="60" aria-hidden="true"><polygon points="0,40 100,15 100,45 5,60" fill="var(--green)"/></svg>

<section class="abs testi">
  <svg style="position:absolute;left:0;top:0" width="1200" height="521" aria-hidden="true">
    <polygon points="0,330 90,290 60,350 0,370" fill="var(--green-soft)"/>
    <polygon points="0,340 40,325 20,370 0,380" fill="var(--green)"/>
    <polygon points="1150,420 1200,395 1200,450 1140,460" fill="var(--green-soft)"/>
  </svg>
</section>
<h2 class="abs sec-title" style="top:3392px">User <span>Testimonials</span></h2>
<div class="abs t-avatar" style="left:291px;top:3489px" role="img" aria-label="Customer photo"></div>
<div class="abs t-avatar" style="left:804px;top:3489px" role="img" aria-label="Customer photo"></div>
<p class="abs t-text" style="left:120px;top:3599px">The report was accurate and gave me a good understanding of my current credit status. I found it interesting the way the scoring worked and really enjoyed reading it...guess because I am doing well with managing credit.</p>
<p class="abs t-text" style="left:631px;top:3599px">The report is well detailed, and gives you all the info that you need. This has helped me to restructure some finances and improve. I would highly recommend using BrightLedgerView.co.za to anyone interested in knowing what their score is.</p>
<div class="abs stars" style="left:288px;top:3700px;font-size:20px">★★★★★</div>
<div class="abs stars" style="left:801px;top:3700px;font-size:20px">★★★★★</div>

<footer class="abs footer">
  <h5 style="left:99px">Terms</h5>
  <a style="left:99px;top:116px">General Terms Of Use</a>
  <a style="left:99px;top:149px">Exclusion Of Liability</a>
  <a style="left:99px;top:182px">Security Policy</a>
  <a style="left:99px;top:215px">Privacy Policy</a>
  <h5 style="left:368px">Purchase</h5>
  <a style="left:368px;top:116px">Delivery Policy</a>
  <a style="left:368px;top:149px">Data Policy</a>
  <a style="left:368px;top:182px">Refund Policy</a>
  <a style="left:368px;top:215px">Charges And Fees</a>
  <h5 style="left:614px">Quick Links</h5>
  <a style="left:614px;top:116px">About Us</a>
  <a style="left:614px;top:149px">Articles</a>
  <a style="left:614px;top:182px">Contact Us</a>
  <a style="left:614px;top:215px">Login</a>
  <h5 style="left:836px">Sign Up For Our Newsletter</h5>
  <div class="news">Email Address
    <svg style="position:absolute;right:6px;top:2px" width="14" height="14"><path d="M1 7l12-6-5 12-2-5z" fill="#fff"/></svg>
  </div>
  <span class="social" style="left:836px;top:163px" aria-label="Social profile"></span>
  <span class="social" style="left:880px;top:163px" aria-label="Social profile"></span>
  <span class="social" style="left:923px;top:163px" aria-label="Social profile"></span>
  <span class="social" style="left:966px;top:163px" aria-label="Social profile"></span>
  <div class="divider"></div>
  <p class="copy">© All Rights Reserved BrightLedgerView.co.za | NCR Reg. No. NCRCB00</p>
  <span class="pay" style="left:871px" aria-label="Accepted payment card"></span>
  <span class="pay" style="left:930px" aria-label="Accepted payment card"></span>
  <span class="pay" style="left:989px" aria-label="Accepted payment card"></span>
  <span class="pay" style="left:1048px" aria-label="Accepted payment card"></span>
</footer>

</body>
</html>
```